Business Cards & Letterhead etc.
Would like our Business Cards designed off our Logo
Professional
Dale Fenwick
PO Box 61309
Linden Falls, OR 97310
fenwickd@quellbridgeco.com
www.quellbridgeco.com
I would like the business cards to be designed so i can later alter the contact info for multiple people. Anything in Adobe is fine.

```html
<!DOCTYPE html>
<html lang="en">
<head>
<meta charset="utf-8">
<title>Quell IT Group – Business Cards</title>
<link href="https://fonts.googleapis.com/css2?family=Oswald:wght@600&family=Open+Sans:wght@400;600;700&display=swap" rel="stylesheet">
<style>
  :root {
    --stage: #5a4f47;
    --card-dark: #19191b;
    --card-black: #0e0e10;
    --silver-light: #d9d9db;
    --silver-mid: #9c9ca0;
    --silver-deep: #6e6e73;
    --accent-blue: #1e6fd0;
    --accent-blue-deep: #0b3f8a;
    --text-light: #ffffff;
    --text-soft: #e4e4e6;
  }
  * { margin: 0; padding: 0; box-sizing: border-box; }
  html, body { width: 1200px; height: 974px; overflow: hidden; }
  body {
    background: var(--stage);
    font-family: "Open Sans", Arial, sans-serif;
    position: relative;
  }
  .card {
    position: absolute;
    width: 630px;
    height: 360px;
    border-radius: 14px;
    overflow: hidden;
    box-shadow: 0 10px 28px rgba(0,0,0,.45);
  }
  .card-front { left: 90px; top: 80px; background: var(--card-dark); }
  .card-back { left: 480px; top: 540px; background: var(--card-black); }
  .card-shapes { position: absolute; inset: 0; width: 100%; height: 100%; }

  .brand {
    position: absolute;
    left: 34px;
    top: 92px;
    width: 210px;
    text-align: center;
  }
  .brand-mark {
    width: 64px; height: 64px;
    border-radius: 50%;
    background: var(--accent-blue);
    margin: 0 auto 14px;
  }
  .brand-name {
    font-family: "Oswald", Arial, sans-serif;
    font-weight: 600;
    font-size: 34px;
    line-height: 1.05;
    letter-spacing: 1px;
    color: var(--text-light);
  }

  .contact {
    position: absolute;
    right: 34px;
    top: 26px;
    width: 260px;
    text-align: right;
    color: var(--text-light);
  }
  .contact-name { font-size: 27px; font-weight: 600; line-height: 1.1; }
  .contact-role { font-size: 12px; color: var(--text-soft); margin-top: 2px; }
  .contact-rule {
    border-top: 2px dotted rgba(255,255,255,.8);
    width: 150px;
    margin: 14px 0 12px auto;
  }
  .contact-address { font-size: 12px; line-height: 1.45; }
  .contact-phones { list-style: none; margin-top: 12px; font-size: 12px; line-height: 1.55; }
  .contact-phones li { display: flex; justify-content: flex-end; align-items: center; gap: 8px; }
  .contact-phones svg { width: 12px; height: 12px; fill: var(--text-light); }
  .contact-email { font-size: 11.5px; margin-top: 18px; }

  .front-url {
    position: absolute;
    right: 34px;
    bottom: 22px;
    font-size: 14px;
    font-weight: 600;
    color: var(--text-light);
  }

  .back-sign {
    position: absolute;
    right: 36px;
    bottom: 70px;
    display: flex;
    align-items: center;
    gap: 10px;
    color: var(--text-light);
    font-size: 14px;
    font-weight: 700;
  }
  .back-sign-mark {
    width: 30px; height: 30px;
    border-radius: 50%;
    background: var(--accent-blue);
  }
</style>
</head>
<body>

<section class="card card-front" aria-label="Business card front">
  <svg class="card-shapes" viewBox="0 0 630 360" preserveAspectRatio="none" aria-hidden="true">
    <defs>
      <linearGradient id="silverPanel" x1="0" y1="0" x2="1" y2="1">
        <stop offset="0" stop-color="#d9d9db"/>
        <stop offset=".45" stop-color="#9c9ca0"/>
        <stop offset="1" stop-color="#6e6e73"/>
      </linearGradient>
      <linearGradient id="blueSweep" x1="0" y1="0" x2="0" y2="1">
        <stop offset="0" stop-color="#1e6fd0"/>
        <stop offset="1" stop-color="#0b3f8a"/>
      </linearGradient>
    </defs>
    <path d="M250 0 C200 110 195 230 255 360 L270 360 C215 235 222 110 270 0 Z" fill="url(#blueSweep)"/>
    <path d="M270 0 C222 110 215 235 270 320 L630 320 L630 0 Z" fill="url(#silverPanel)"/>
    <path d="M270 320 L630 320 L630 360 L290 360 C282 347 276 334 270 320 Z" fill="#19191b"/>
  </svg>

  <div class="brand">
    <div class="brand-mark"></div>
    <div class="brand-name">QUELL<br>IT GROUP</div>
  </div>

  <div class="contact">
    <p class="contact-name">Dale Fenwick</p>
    <p class="contact-role">Owner</p>
    <div class="contact-rule"></div>
    <p class="contact-address">PO Box 61309<br>Linden Falls, OR 97310</p>
    <ul class="contact-phones">
      <li>800-555-0142
        <svg viewBox="0 0 24 24"><path d="M6.6 10.8a15 15 0 0 0 6.6 6.6l2.2-2.2c.3-.3.7-.4 1-.2 1.1.4 2.3.6 3.6.6.6 0 1 .4 1 1V20c0 .6-.4 1-1 1A17 17 0 0 1 3 4c0-.6.4-1 1-1h3.5c.6 0 1 .4 1 1 0 1.3.2 2.5.6 3.6.1.3 0 .7-.2 1z"/></svg>
      </li>
      <li>800-555-0187
        <svg viewBox="0 0 24 24"><path d="M7 1h10a2 2 0 0 1 2 2v18a2 2 0 0 1-2 2H7a2 2 0 0 1-2-2V3a2 2 0 0 1 2-2zm0 3v14h10V4z"/></svg>
      </li>
      <li>800-555-0193
        <svg viewBox="0 0 24 24"><path d="M2 5h20v14H2zm2 2v.5l8 5 8-5V7zm0 2.8V17h16V9.8l-8 5z"/></svg>
      </li>
    </ul>
    <p class="contact-email">fenwickd@quellbridgeco.com</p>
  </div>

  <p class="front-url">www.quellbridgeco.com</p>
</section>

<section class="card card-back" aria-label="Business card back">
  <div class="back-sign">
    <span class="back-sign-mark"></span>
    <span>www.quellbridgeco.com</span>
  </div>
</section>

</body>
</html>
```